PowerPoint Master for IT company (lumoGrid GmbH)

As IT company we work in the fields Mobile, Big Data, Predictive Maintenance, Industry 4.0 and Data Science for the german Rail company "Nordwerk Schiene". We already have a Logo, coloring and a website (Attached Files).

What we need is a clear, professional and simple Design (nothing fancy) for PowerPoint/Word Master and Business Cards. Stockphotos from https://bildarchiv.nordwerkschiene.example/ can be used beside the attached logos.

We are a german company but would need either an universal or DE and EN template for PoerPoint.

Target Market(s)

IT, B2B, Rail companies, Industry

Contact Information for Business Card

- Logo
- Company Name
- Name
- Position
- Address
- Phone
- Mail

Font styles to use
Sans Serif

```html
<!DOCTYPE html>
<html lang="en">
<head>
<meta charset="utf-8">
<title>lumoGrid GmbH – PowerPoint Master</title>
<link href="https://fonts.googleapis.com/css2?family=Arimo:wght@400;700&display=swap" rel="stylesheet">
<style>
:root{
  --canvas:#ececec;
  --slide:#ffffff;
  --navy:#1c1c5a;
  --head:#27407f;
  --row:#e6e6ec;
  --rule:#e3e3e8;
  --ink:#2a2a2a;
  --map:#a9a6a6;
  --white:#ffffff;
}
*{margin:0;padding:0;box-sizing:border-box}
html,body{width:1200px;height:1050px;overflow:hidden}
body{background:var(--canvas);font-family:"Arimo",Arial,sans-serif;color:var(--ink);position:relative}
.slide{position:absolute;width:516px;height:290px;background:var(--slide);overflow:hidden}
.slide--table{left:67px;top:69px}
.slide--map{left:615px;top:69px}
.slide--closing{left:67px;top:380px}
.slide__title{position:absolute;left:16px;top:20px;font-size:18px;font-weight:400}
.slide__rule{position:absolute;left:16px;right:16px;top:46px;height:1px;background:var(--rule)}
.footer{position:absolute;left:0;right:0;bottom:0;height:20px;background:var(--navy);color:var(--white)}
.footer__client{position:absolute;left:16px;top:7px;font-size:5px;font-weight:700;letter-spacing:.2px;white-space:nowrap}
.footer__brand{position:absolute;right:16px;top:6px;display:flex;align-items:center;gap:3px;font-size:7px;font-weight:400;letter-spacing:.3px}
.footer__dot{width:8px;height:8px;border-radius:50%;background:var(--white)}
.data-table{position:absolute;left:16px;top:61px;width:484px;border-collapse:collapse;table-layout:fixed}
.data-table th{background:var(--head);color:var(--white);font-size:7.5px;font-weight:700;text-align:left;height:17px;padding-left:4px;border-left:1px solid var(--white)}
.data-table td{font-size:6.5px;height:18.7px;padding-left:4px;border-left:1px solid var(--white)}
.data-table th:first-child,.data-table td:first-child{border-left:0}
.data-table tbody tr:nth-child(even) td{background:var(--row)}
.slide__base-rule{position:absolute;left:16px;right:16px;top:248px;height:1px;background:#b9b9c2}
.world-map{position:absolute;left:93px;top:70px;width:332px;height:180px;background:var(--map);border-radius:40% 45% 35% 40%/45% 40% 50% 45%}
.closing__photo{position:absolute;inset:0;background:linear-gradient(135deg,#9fc6ef 0%,#6b8fcf 40%,#3c4c9a 72%,#1e2060 100%)}
.closing__title{position:absolute;right:23px;top:174px;font-size:38px;font-weight:700;color:var(--white);letter-spacing:0}
.closing__line{position:absolute;left:329px;right:23px;top:224px;height:1.5px;background:var(--white)}
</style>
</head>
<body>
<section class="slide slide--table">
  <h2 class="slide__title">Table</h2>
  <div class="slide__rule"></div>
  <table class="data-table">
    <thead><tr><th>Text here</th><th>Text here</th><th>Text here</th><th>Text here</th><th>Text here</th><th>Text here</th></tr></thead>
    <tbody>
      <tr><td>Text here</td><td>Text here</td><td>Text here</td><td>Text here</td><td>Text here</td><td>Text here</td></tr>
      <tr><td></td><td></td><td></td><td></td><td></td><td></td></tr>
      <tr><td></td><td></td><td></td><td></td><td></td><td></td></tr>
      <tr><td></td><td></td><td></td><td></td><td></td><td></td></tr>
      <tr><td></td><td></td><td></td><td></td><td></td><td></td></tr>
      <tr><td></td><td></td><td></td><td></td><td></td><td></td></tr>
      <tr><td></td><td></td><td></td><td></td><td></td><td></td></tr>
      <tr><td></td><td></td><td></td><td></td><td></td><td></td></tr>
    </tbody>
  </table>
  <div class="slide__base-rule"></div>
  <footer class="footer">
    <div class="footer__client">Nordwerk Schiene</div>
    <div class="footer__brand">LUMOGRID<span class="footer__dot"></span></div>
  </footer>
</section>

<section class="slide slide--map">
  <h2 class="slide__title">Map</h2>
  <div class="slide__rule"></div>
  <div class="world-map" role="img" aria-label="Grey world map showing all continents"></div>
  <footer class="footer">
    <div class="footer__client">Nordwerk Schiene</div>
    <div class="footer__brand">LUMOGRID<span class="footer__dot"></span></div>
  </footer>
</section>

<section class="slide slide--closing">
  <div class="closing__photo" role="img" aria-label="Blurred photo of a team raising hands, tinted in blue"></div>
  <h2 class="closing__title">THANK YOU!</h2>
  <div class="closing__line"></div>
</section>
</body>
</html>
```